Kessler MD Summit Primary Care Business Card

Need a business card for a medical clinic targeting VIP patients. Should portray an upscale feeling. Simple, clean design. Logo and colors need to be incorporated into card. Clinic colors are gray/ silver, blues, white same as logo.
Clinic is a cash only VIP service clinic targeting higher income patients.
Tagline: "Where every visit is personal - Care Without Compromise"

Target Market(s)

VIP, upscale

Industry/Entity Type

Medical

Contact Information for Business Card

Would like to use for cards with raised print or metallic highlight.

Requirements
Must have
• Incorporate logo, Use colors in logo
Nice to have
• Metallic detail
Should not have
• too much details or colors, other stock photos or designs

```html
<!DOCTYPE html>
<html lang="en">
<head>
<meta charset="utf-8">
<title>Kessler MD Summit Primary Care – Business Card</title>
<link rel="stylesheet" href="https://fonts.googleapis.com/css2?family=Libre+Baskerville:wght@400;700&display=swap">
<style>
  :root {
    --page: #e9e8e5;
    --navy: #3f5673;
    --navy-light: #5a7392;
    --silver: #b9bcc0;
    --silver-dark: #8d9196;
    --paper: #f7f7f6;
    --ink: #4a5d78;
    --ink-soft: #7b8594;
    --back-top: #c3c7cb;
    --back-bottom: #8f959b;
    --white: #ffffff;
  }
  * { box-sizing: border-box; margin: 0; padding: 0; }
  html, body { width: 1200px; height: 780px; overflow: hidden; }
  body {
    background: var(--page);
    font-family: "Libre Baskerville", Georgia, serif;
    position: relative;
  }
  .card {
    position: absolute;
    top: 240px;
    width: 520px;
    height: 300px;
    border-radius: 18px;
    overflow: hidden;
    box-shadow: 0 10px 26px rgba(0,0,0,.18);
  }
  .card--front { left: 50px; background: var(--paper); }
  .card--back {
    left: 630px;
    background: linear-gradient(160deg, var(--back-top), var(--back-bottom));
  }
  .front-band { position: absolute; inset: 0; }
  .holder {
    position: absolute; right: 34px; top: 22px;
    color: var(--white); text-align: right;
  }
  .holder__name { font-size: 17px; font-weight: 700; letter-spacing: .5px; }
  .holder__role { font-size: 12px; margin-top: 2px; }
  .brand {
    position: absolute; left: 40px; top: 148px;
    color: var(--ink);
  }
  .brand__name {
    font-size: 17px; letter-spacing: 1px; display: flex; align-items: center; gap: 10px;
  }
  .brand__name::before {
    content: ""; width: 28px; height: 1px; background: var(--ink-soft);
  }
  .brand__sub { font-size: 15px; font-weight: 700; letter-spacing: .8px; margin-top: 4px; margin-left: 38px; }
  .contacts {
    position: absolute; left: 40px; bottom: 30px;
    display: flex; align-items: stretch; gap: 16px;
    color: var(--ink-soft); font-size: 11px;
  }
  .contacts__group { display: flex; flex-direction: column; gap: 6px; }
  .contacts__row { display: flex; align-items: center; gap: 7px; white-space: nowrap; }
  .contacts__divider { width: 1px; background: var(--ink); }
  .icon { width: 14px; height: 14px; flex: none; }
  .back-brand {
    position: absolute; left: 0; right: 0; top: 110px;
    text-align: center; color: var(--white);
  }
  .back-brand__name {
    font-size: 22px; letter-spacing: 1.5px;
    display: flex; align-items: center; justify-content: center; gap: 12px;
  }
  .back-brand__name::before,
  .back-brand__name::after { content: ""; width: 30px; height: 1px; background: var(--white); }
  .back-brand__sub { font-size: 18px; font-weight: 700; letter-spacing: 1px; margin-top: 6px; }
  .tagline {
    position: absolute; left: 0; right: 0; bottom: 34px;
    text-align: center; color: var(--white); font-size: 13px; letter-spacing: .4px;
    white-space: nowrap;
  }
</style>
</head>
<body>
  <section class="card card--front" aria-label="Card front">
    <svg class="front-band" viewBox="0 0 520 300" preserveAspectRatio="none" aria-hidden="true">
      <defs>
        <linearGradient id="bandFill" x1="0" y1="0" x2="1" y2="0">
          <stop offset="0" stop-color="#3f5673"/>
          <stop offset="1" stop-color="#5a7392"/>
        </linearGradient>
      </defs>
      <path d="M0 0 H520 V96 C380 70 180 70 0 150 Z" fill="url(#bandFill)"/>
      <path d="M0 150 C180 70 380 70 520 96 V108 C380 82 180 84 0 164 Z" fill="#ffffff"/>
      <path d="M0 164 C180 84 380 82 520 108 V118 C380 94 180 98 0 172 Z" fill="#b9bcc0"/>
    </svg>
    <div class="holder">
      <div class="holder__name">OWEN HARTLEY</div>
      <div class="holder__role">Founder</div>
    </div>
    <div class="brand">
      <div class="brand__name">KESSLER MD</div>
      <div class="brand__sub">SUMMIT PRIMARY CARE</div>
    </div>
    <div class="contacts">
      <div class="contacts__group">
        <div class="contacts__row">
          <svg class="icon" viewBox="0 0 14 14" aria-hidden="true"><circle cx="7" cy="7" r="6.3" fill="none" stroke="#4a5d78"/><rect x="4.8" y="3.4" width="4.4" height="7.2" rx="0.8" fill="none" stroke="#4a5d78" stroke-width="1"/></svg>
          (555) 318-2046
        </div>
        <div class="contacts__row">
          <svg class="icon" viewBox="0 0 14 14" aria-hidden="true"><circle cx="7" cy="7" r="6.3" fill="none" stroke="#4a5d78"/><path d="M4 6 Q7 3.5 10 6 L9.3 7.2 L8.2 6.8 V6 H5.8 V6.8 L4.7 7.2 Z M4.6 8 H9.4 V10 H4.6 Z" fill="#4a5d78"/></svg>
          (555) 318-2047
        </div>
      </div>
      <span class="contacts__divider"></span>
      <div class="contacts__group">
        <div class="contacts__row">
          <svg class="icon" viewBox="0 0 14 14" aria-hidden="true"><circle cx="7" cy="7" r="6.3" fill="none" stroke="#4a5d78"/><rect x="3.6" y="4.6" width="6.8" height="4.8" fill="none" stroke="#4a5d78" stroke-width="1"/><path d="M3.6 4.6 L7 7.4 L10.4 4.6" fill="none" stroke="#4a5d78" stroke-width="1"/></svg>
          desk@kesslermd.com
        </div>
        <div class="contacts__row">
          <svg class="icon" viewBox="0 0 14 14" aria-hidden="true"><circle cx="7" cy="7" r="6.3" fill="none" stroke="#4a5d78"/><circle cx="7" cy="7" r="3.6" fill="none" stroke="#4a5d78" stroke-width="1"/><path d="M3.4 7 H10.6 M7 3.4 V10.6" stroke="#4a5d78" stroke-width="0.8"/></svg>
          www.kesslermd.com
        </div>
      </div>
      <span class="contacts__divider"></span>
      <div class="contacts__group">
        <div class="contacts__row">PO Box 418 Harbour Lane</div>
        <div class="contacts__row">Geelong</div>
      </div>
    </div>
  </section>

  <section class="card card--back" aria-label="Card back">
    <div class="back-brand">
      <div class="back-brand__name">KESSLER MD</div>
      <div class="back-brand__sub">SUMMIT PRIMARY CARE</div>
    </div>
    <p class="tagline">Where every visit is personal - Care Without Compromise</p>
  </section>
</body>
</html>
```